Wordpress Theme for a Professional Speaker's Website

I I need a website to promote myself as a speaker to corporations and meeting planners. Some examples of similar sites I like are:

http://www.beginwithpurpose.example (this is by far my favorite)
http://www.tovaruskin.example
http://www.glenbeckworth.example
http://www.lomtrisel.example
http://www.dawnafterstorms.example
http://www.osricpellandine.example

I like modern, minimalistic, innovative. I'm okay if it's edgy but still want it communicate professionalism.

The primary objective is to position me as an expert who can deliver valuable information in an entertaining manner.

There are two calls to action. The first is to capture name and email address to subscribe to my newsletter. The second is to request more information about booking me to speak for their company, organization, etc.

The pages on the website will ultimately be the following:

1. Home (should include sections for recent blog posts, featured topics/presentations, short bio, testimonials, email capture, and anything else you think should be added.
2. Meet Ross
3. Blog
4. Keynotes & Speaking
5. Training & Webinars
6. Coaching & Consulting
7. Testimonials
8. Book Ross
9. Media Inquiries
10. Contact

Please feel free to use your creativity. I don't want my requirements to limit you in any way. I'm just looking for a modern, professional site that will make me stand out from the crowd.

I don't have any existing site or brand identity. My plan is to have the website design I ultimately choose serve as the foundation for the rest of my brand identity.

Target Market(s)

Corporate meeting planners and executives

Industry/Entity Type

It Professional

Font styles to use
Sans Serif

Requirements
Must have
• Email capture, testimonials, blog
Nice to have
• None
Should not have
• None

```html
<!DOCTYPE html>
<html lang="en">
<head>
<meta charset="utf-8">
<title>Ross Varello — Professional Speaker</title>
<link href="https://fonts.googleapis.com/css2?family=Open+Sans:wght@400;600;700;800&family=Roboto+Slab:wght@300;400;700&family=Noto+Serif:ital@1&display=swap" rel="stylesheet">
<style>
:root{
  --teal:#1b8fb1;
  --teal-dark:#16738f;
  --teal-deep:#135f78;
  --orange:#ee6a25;
  --rust:#c4561e;
  --ink:#1d1d1d;
  --grey-band:#e8e7e2;
  --text:#444;
  --white:#fff;
  --black:#0c0c0c;
}
*{box-sizing:border-box;margin:0;padding:0}
html,body{width:1200px;height:3564px;overflow:hidden}
body{position:relative;font-family:"Open Sans",Arial,sans-serif;color:var(--text);background:var(--white)}
.abs{position:absolute}
.slab{font-family:"Roboto Slab",Georgia,serif}

/* header */
.site-header{left:0;top:0;width:1200px;height:102px;background:var(--white)}
.brand{left:88px;top:24px;font-size:40px;font-weight:700;letter-spacing:.5px;color:var(--orange);line-height:50px}
.brand .first{color:var(--teal)}
.top-links{left:587px;top:40px;font-size:14px;color:#333;word-spacing:2px}
.top-links span{margin:0 8px;color:#999}
.phone-cta{left:867px;top:24px;width:247px;height:54px;background:var(--orange);display:flex;align-items:center}
.phone-cta .icon{width:50px;height:54px;background:var(--teal);display:flex;align-items:center;justify-content:center}
.phone-cta .num{flex:1;text-align:center;color:var(--white);font-size:28px;font-weight:600}

.main-nav{left:0;top:102px;width:1200px;height:60px;background:var(--teal);display:flex;padding-left:64px}
.main-nav a{color:var(--white);font-size:13px;font-weight:700;text-decoration:none;line-height:60px;padding:0 15px;letter-spacing:.2px}
.main-nav a.active{background:#45a8c6}

/* hero */
.hero{left:0;top:162px;width:1200px;height:439px;background:radial-gradient(ellipse at 75% 40%,#6a6058 0%,#3a3532 45%,#1b1a19 100%)}
.hero-title{left:135px;top:100px;color:var(--white);font-size:56px;font-weight:800;line-height:82px;letter-spacing:.5px}
.booking-bar{left:0;top:601px;width:1200px;height:74px;background:var(--black)}
.booking-bar p{position:absolute;left:188px;top:20px;color:var(--white);font-size:29px}
.btn-book{left:817px;top:601px;width:240px;height:74px;background:var(--orange);color:var(--white);font-size:28px;text-align:center;line-height:74px}

.subscribe{left:0;width:1200px;background:var(--grey-band)}
.subscribe .label{position:absolute;font-size:24px;color:#333;font-weight:600}
.field{position:absolute;height:42px;background:var(--white);border:1px solid #3aa0bd;font-size:14px;color:#888;padding-left:16px;line-height:40px}
.btn-submit{position:absolute;height:42px;color:var(--white);font-size:16px;font-weight:700;text-align:center;line-height:42px}

/* videos */
.section-title{width:1200px;left:0;text-align:center;font-size:26px;color:#333;font-weight:300}
.section-title strong{color:var(--teal);font-weight:700}
.section-lead{left:240px;width:720px;text-align:center;font-size:12.5px;line-height:24px;color:#555}
.video-card{top:943px;width:316px;height:209px;background:var(--black);border-radius:4px;overflow:hidden}
.video-card .thumb{position:absolute;left:4px;top:4px;right:4px;height:164px;background:linear-gradient(160deg,#7a5a45,#3c2c23 60%,#1e1714)}
.video-card .play{position:absolute;left:126px;top:52px}
.video-card .caption{position:absolute;left:0;right:0;bottom:8px;text-align:center;color:var(--white);font-size:17px}
.btn{color:var(--white);font-size:14px;font-weight:700;text-align:center;letter-spacing:.3px}
.btn-more-videos{left:499px;top:1207px;width:202px;height:48px;line-height:48px;background:var(--orange)}

/* about */
.about-bg{left:0;top:1224px}
.about-photo{left:238px;top:1366px;width:320px;height:447px;background:linear-gradient(180deg,#2a5577,#1c2f4a 70%,#16253a);border-radius:140px 140px 0 0}
.about-title{left:611px;top:1428px;color:var(--white);font-size:25px}
.about-title strong{font-weight:700}
.about-text{left:611px;top:1486px;width:420px;color:var(--white);font-size:12.5px;line-height:21px}
.btn-outline{background:var(--white);color:var(--teal);font-weight:700;text-align:center}
.btn-know{left:611px;top:1680px;width:149px;height:45px;line-height:45px;font-size:14px}

/* blog */
.blog-heading{top:1884px}
.blog-heading strong{color:var(--orange)}
.tile{width:600px;height:378px}
.tile-text{position:absolute;color:var(--white)}
.tile-text h3{font-size:24px;font-weight:700;margin-bottom:18px}
.tile-text p{font-size:13px;line-height:21px;width:440px}
.btn-read{display:block;margin-top:32px;width:126px;height:50px;line-height:50px;font-size:16px;color:var(--rust)}

/* testimonials */
.testimonials{left:0;top:2709px;width:1200px;height:527px;background:radial-gradient(ellipse at 50% 40%,#2c2c2c,#141414 70%,#0a0a0a)}
.testimonials .section-title{color:var(--white);top:76px}
.testimonials .section-title strong{color:var(--orange)}
.avatar{width:110px;height:110px;border-radius:50%;background:linear-gradient(160deg,#b9a796,#6b5848);border:4px solid #ddd}
.quote{width:350px;color:var(--white);font-family:"Noto Serif",Georgia,serif;font-style:italic;font-size:12.5px;line-height:21px}
.quote .by{margin-top:12px;color:#ddd}
.quote .by span{color:var(--teal)}
.dots{left:583px;top:3061px;display:flex;gap:6px}
.dots i{width:12px;height:12px;border-radius:50%;background:#555}
.dots i.on{background:var(--orange)}
.btn-testimonials{left:482px;top:3122px;width:250px;height:48px;line-height:48px;background:var(--teal)}

/* footer */
.site-footer{left:0;top:3322px;width:1200px;height:242px;background:var(--black)}
.footer-col{top:3352px}
.footer-col h4{color:var(--teal);font-size:19px;font-weight:700;margin-bottom:8px}
.footer-col a{display:block;color:#777;font-size:12.5px;line-height:26px;text-decoration:none}
.footer-brand{left:870px;top:3345px;color:var(--teal);font-size:33px}
.footer-phone{left:870px;top:3393px;color:#777;font-size:29px;display:flex;align-items:center;gap:10px}
.footer-mail{left:870px;top:3437px;color:#777;font-size:13px;display:flex;align-items:center;gap:12px}
.footer-rule{left:124px;top:3507px;width:1010px;height:1px;background:#2a2a2a}
.copyright{left:130px;top:3527px;color:#666;font-size:12px}
.follow{left:827px;top:3522px;display:flex;align-items:center;gap:12px;color:#666;font-size:12px}
.follow i{width:24px;height:24px;border-radius:50%;background:#666}
</style>
</head>
<body>

<header class="abs site-header">
  <div class="abs brand"><span class="first">ROSS</span> VARELLO</div>
  <div class="abs top-links">Media Inquiries<span>|</span>Contact<span>|</span>For Booking:</div>
  <div class="abs phone-cta">
    <div class="icon"><svg width="18" height="30" viewBox="0 0 18 30"><rect x="1.5" y="1.5" width="15" height="27" rx="3" fill="none" stroke="#fff" stroke-width="3"/><rect x="6" y="23" width="6" height="2" fill="#fff"/></svg></div>
    <div class="num">555.010.4821</div>
  </div>
</header>

<nav class="abs main-nav">
  <a class="active">HOME</a><a>MEET ROSS</a><a>BLOG</a><a>KEYNOTES &amp; SPEAKING</a><a>TRAINING &amp; WEBINARS</a><a>COACHING &amp; CONSULTING</a><a>TESTIMONIALS</a><a>BOOK ROSS</a>
</nav>

<section class="abs hero" role="img" aria-label="Photo of the speaker on stage addressing a large audience">
  <h1 class="abs hero-title">YESSS'<br>LET'S DO HIM.<br>CLARITY &amp; CONVICTION</h1>
</section>
<div class="abs booking-bar"><p>Do book him in advance to avoid hassle later.</p></div>
<div class="abs btn-book">Book Ross</div>

<form class="abs subscribe" style="top:675px;height:73px">
  <div class="label" style="left:135px;top:20px;font-size:22px">Subscribe Us:</div>
  <div class="field" style="left:292px;top:16px;width:316px">Your Name</div>
  <div class="field" style="left:625px;top:16px;width:318px">Email Address</div>
  <div class="btn-submit" style="left:962px;top:16px;width:95px;background:var(--teal)">Submit</div>
</form>

<h2 class="abs section-title slab" style="top:816px">Check his latest <strong>Speaks</strong> presentation</h2>
<p class="abs section-lead" style="top:858px">Lorem ipsum dolor sit amet, consectetur adipisicing elit, sed do eiusmod tempor incididunt ut labore et dolore magna aliqua. Ut enim ad minim veniam, quis nostrud exercitation ullamco laboris nisi ut aliquip ex ea commodo consequat.</p>

<div class="abs about-bg">
  <svg width="1200" height="589" viewBox="0 0 1200 589">
    <defs><linearGradient id="tealFill" x1="0" y1="0" x2="1" y2="1"><stop offset="0" stop-color="#1d87a6"/><stop offset="1" stop-color="#145f78"/></linearGradient></defs>
    <path d="M0 0 L599 118 L1200 0 L1200 589 L0 589 Z" fill="url(#tealFill)"/>
  </svg>
</div>

<article class="abs video-card" style="left:97px"><div class="thumb" role="img" aria-label="Video still of a conference audience"></div>
  <svg class="play" width="62" height="62" viewBox="0 0 62 62"><circle cx="31" cy="31" r="31" fill="#222" opacity=".85"/><path d="M25 19 L44 31 L25 43 Z" fill="var(--orange)"/></svg>
  <div class="caption">Meeting Name Here</div></article>
<article class="abs video-card" style="left:442px"><div class="thumb" role="img" aria-label="Video still of seated meeting attendees" style="background:linear-gradient(160deg,#d9d4cc,#8d8277 60%,#4c433c)"></div>
  <svg class="play" width="62" height="62" viewBox="0 0 62 62"><circle cx="31" cy="31" r="31" fill="#222" opacity=".85"/><path d="M25 19 L44 31 L25 43 Z" fill="var(--orange)"/></svg>
  <div class="caption">Meeting Name Here</div></article>
<article class="abs video-card" style="left:786px"><div class="thumb" role="img" aria-label="Video still of a full lecture hall" style="background:linear-gradient(160deg,#9b7a58,#5e4632 60%,#2b2018)"></div>
  <svg class="play" width="62" height="62" viewBox="0 0 62 62"><circle cx="31" cy="31" r="31" fill="#222" opacity=".85"/><path d="M25 19 L44 31 L25 43 Z" fill="var(--orange)"/></svg>
  <div class="caption">Meeting Name Here</div></article>

<div class="abs btn btn-more-videos">SEE MORE VIDEOS</div>

<div class="abs about-photo" role="img" aria-label="Portrait of Ross Varello in a suit, arms crossed"></div>
<h2 class="abs about-title slab"><strong>About</strong> Ross Varello</h2>
<p class="abs about-text">Lorem ipsum dolor sit amet, consectetur adipisicing elit, sed do eiusmod tempor incididunt ut labore et dolore magna aliqua. Ut enim ad minim veniam, quis nostrud exercitation ullamco laboris nisi ut aliquip ex ea commodo consequat. Duis aute irure dolor in reprehenderit in voluptate velit esse cillum dolore eu fugiat nulla pariatur. Excepteur sint occaecat cupidatat non proident, sunt in culpa qui officia deserunt mollit anim id est laborum.</p>
<div class="abs btn-outline btn-know">KNOW MORE</div>

<h2 class="abs section-title slab blog-heading">Our recent <strong>Blog</strong> post</h2>

<article class="abs tile" style="left:0;top:1953px;background:linear-gradient(135deg,#cf5f24,#b44d1a)">
  <div class="tile-text" style="left:95px;top:80px">
    <h3>Some blog headline goes here</h3>
    <p>Lorem ipsum dolor sit amet, consectetur adipisicing elit, sed do eiusmod tempor incididunt ut labore et dolore magna aliqua. Ut enim ad minim veniam, quis nostrud exercitation ullamco laboris nisi ut aliquip ex ea commodo consequat.</p>
    <span class="btn-outline btn-read">Read More</span>
  </div>
</article>
<div class="abs tile" style="left:600px;top:1953px;background:radial-gradient(ellipse at 60% 40%,#6d6d6d,#2b2b2b 70%,#151515)" role="img" aria-label="Gold microphone in front of a blurred audience"></div>
<svg class="abs" style="left:600px;top:2124px" width="16" height="34" viewBox="0 0 16 34"><path d="M0 0 L16 17 L0 34 Z" fill="#b44d1a"/></svg>

<div class="abs tile" style="left:0;top:2331px;background:linear-gradient(160deg,#9fb9cf,#5a7896 55%,#2f3d4f)" role="img" aria-label="Speaker surrounded by reporters holding microphones"></div>
<article class="abs tile" style="left:600px;top:2331px;background:linear-gradient(135deg,#1b86a6,#156a86)">
  <div class="tile-text" style="left:68px;top:80px">
    <h3>Some blog headline goes here</h3>
    <p>Lorem ipsum dolor sit amet, consectetur adipisicing elit, sed do eiusmod tempor incididunt ut labore et dolore magna aliqua. Ut enim ad minim veniam, quis nostrud exercitation ullamco laboris nisi ut aliquip ex ea commodo consequat.</p>
    <span class="btn-outline btn-read" style="color:var(--teal)">Read More</span>
  </div>
</article>

<section class="abs testimonials">
  <h2 class="abs section-title slab">What people are <strong>Saying</strong></h2>
</section>
<div class="abs avatar" style="left:78px;top:2875px" role="img" aria-label="Client portrait"></div>
<blockquote class="abs quote" style="left:221px;top:2870px">Lorem ipsum dolor sit amet, consectetur adipisicing elit, sed do eiusmod tempor incididunt ut labore et dolore magna aliqua. Ut enim ad minim veniam, quis nostrud exercitation ullamco laboris nisi ut
  <div class="by"><span>Alder Finch</span>, CEO - ABC Ltd.</div></blockquote>
<div class="abs avatar" style="left:646px;top:2875px" role="img" aria-label="Client portrait"></div>
<blockquote class="abs quote" style="left:789px;top:2870px">Lorem ipsum dolor sit amet, consectetur adipisicing elit, sed do eiusmod tempor incididunt ut labore et dolore magna aliqua. Ut enim ad minim veniam, quis nostrud exercitation ullamco laboris nisi ut
  <div class="by"><span>Alder Finch</span>, CEO - ABC Ltd.</div></blockquote>
<div class="abs dots"><i class="on"></i><i></i><i></i></div>
<div class="abs btn btn-testimonials">SEE MORE TESTIMONIALS</div>

<form class="abs subscribe" style="top:3236px;height:86px">
  <div class="label" style="left:124px;top:24px;font-size:27px;color:#666">Subscribe Us:</div>
  <div class="field" style="left:311px;top:22px;width:314px;border-color:#bbb">Your Name</div>
  <div class="field" style="left:644px;top:22px;width:314px;border-color:#bbb">Email Address</div>
  <div class="btn-submit" style="left:977px;top:22px;width:95px;background:var(--orange)">Submit</div>
</form>

<footer class="abs site-footer"></footer>
<nav class="abs footer-col" style="left:133px"><h4>Sitemap</h4><a>Home</a><a>Meet Ross</a><a>Blog</a><a>Testimonials</a></nav>
<nav class="abs footer-col" style="left:352px"><h4>Learn</h4><a>Keynotes &amp; Speaking</a><a>Training &amp; Webinars</a><a>Coaching &amp; Consulting</a></nav>
<nav class="abs footer-col" style="left:615px"><h4>Get in Touch</h4><a>Book Ross</a><a>Media Inquiries</a><a>Contact</a></nav>
<div class="abs footer-brand">Ross Varello</div>
<div class="abs footer-phone"><svg width="14" height="24" viewBox="0 0 14 24"><rect x="1" y="1" width="12" height="22" rx="2" fill="none" stroke="#777" stroke-width="2"/></svg>555.010.4821</div>
<div class="abs footer-mail"><svg width="16" height="12" viewBox="0 0 16 12"><rect width="16" height="12" fill="#777"/><path d="M0 0 L8 7 L16 0" fill="none" stroke="#000" stroke-width="1.5"/></svg>spk.ross@mail.example</div>
<div class="abs footer-rule"></div>
<div class="abs copyright">© Copyright 2016, Ross Varello. All Rights are Reserved.</div>
<div class="abs follow">Follow Us<i></i><i></i><i></i><i></i><i></i></div>

</body>
</html>
```